8 ft Straight Tension Fabric Display

We’d like you to take the above design and format it for
a narrower banner. Thanks for all your hard work. If possible, you can add another engineering image into the background, something that refers to optics or software.

Remove the wording “innovative products superlative development, high quality analytical instrumentation.”
Instead, add the following list:

Custom Development of
Instruments and Software for:

Point-of-Care Readers
Lateral Flow Strips
Fluorescence
PCR
Thermal Activation
Fluidic Control
Electrochemistry
Immunoassays

Keep the words toward the top part of the sign so that they are more at standing reader height. You can take out “Qelta Optic” and just leave the website at the bottom so there will be more room for the list.

Here are the dimensions for the banner and the instructions from Brisk Tide Signs:

33″ x 81″ Deluxe Retractable Banner

Artwork Upload Size – 33″ (Width) x 81″ (Height)

Safety Margins: (To ensure all graphic elements appear)
* Top: 1″
* Bottom: 3″

We only accept these file formats: jpg, pdf, png, ai, eps, psd
Please make sure your artwork size is the same exact size of your order. Also,do not include any bleed or crop marks.
Max File Size: 300mb

https://www.brisktidesigns.example/product/deluxe-retractable-banner-33-x-81/

Target Market(s)

technology conference

Industry/Entity Type

Medical And Science

Font styles to use
Serif
Sans Serif

Requirements
Must have
• logo
• company name, "Qelta Optic"
• phrases :
• "innovative products, superlative development"
• "high quality analytical instrumentation"
• Must match the size for the 8ft tension fabric display. Final file should be in PDF form. Single-sided display.
Nice to have
• Gold – #786D2E rgba(120, 109, 46, 1) hsla(51, 45%, 33%, 1)
• Teal- #207B75 rgba(32, 123, 117, 1) hsla(176, 59%, 30%, 1)
• Burgundy - #621515 rgba(98, 21, 21, 1) hsla(0, 65%, 23%, 1)

```html
<!DOCTYPE html>
<html lang="en">
<head>
<meta charset="utf-8">
<title>Qelta Optic – 33 x 81 Retractable Banner</title>
<link rel="stylesheet" href="https://fonts.googleapis.com/css2?family=Montserrat:wght@500;600;700&display=swap">
<style>
  :root {
    --burgundy: #9b1c1e;
    --teal-dark: #0b3a33;
    --teal: #207b75;
    --teal-bright: #5cf2f0;
    --gold: #786d2e;
    --gold-band: #c7b64c;
    --yellow-band: #f3f07a;
    --panel-grey: #e4e6e6;
    --base-grey: #e2e2e2;
    --edge-teal: #2a6b6c;
    --stage: #f3f3f3;
    --white: #ffffff;
  }
  html, body {
    margin: 0;
    padding: 0;
    width: 1200px;
    height: 1200px;
    overflow: hidden;
    background: var(--stage);
  }
  .banner {
    position: absolute;
    top: 0;
    left: 355px;
    width: 489px;
    height: 1200px;
    overflow: hidden;
    box-shadow: 0 0 0 1px #d6d6d6;
  }
  .banner svg { display: block; }
  .headline {
    font-family: "Montserrat", sans-serif;
    font-weight: 700;
    font-size: 15px;
    fill: var(--white);
  }
  .service-list {
    font-family: "Montserrat", sans-serif;
    font-weight: 700;
    font-size: 17px;
    fill: var(--gold);
  }
  .website {
    font-family: "Montserrat", sans-serif;
    font-weight: 600;
    font-size: 14px;
    fill: var(--white);
    letter-spacing: 0.3px;
  }
</style>
</head>
<body>
<div class="banner">
  <svg width="489" height="1200" viewBox="0 0 330 810" xmlns="http://www.w3.org/2000/svg">
    <defs>
      <linearGradient id="labPhotoTone" x1="0" y1="0" x2="1" y2="1">
        <stop offset="0" stop-color="#9ea3a6"/>
        <stop offset="0.5" stop-color="#d2d5d7"/>
        <stop offset="1" stop-color="#eceeef"/>
      </linearGradient>
      <linearGradient id="opticsTone" x1="0" y1="0" x2="1" y2="0">
        <stop offset="0" stop-color="#cfdedd"/>
        <stop offset="0.5" stop-color="#e6ecec"/>
        <stop offset="1" stop-color="#d3e3e2"/>
      </linearGradient>
      <linearGradient id="tealWave" x1="0" y1="0" x2="1" y2="0">
        <stop offset="0" stop-color="var(--teal-dark)"/>
        <stop offset="0.5" stop-color="var(--teal)"/>
        <stop offset="1" stop-color="var(--teal-bright)"/>
      </linearGradient>
      <linearGradient id="goldWave" x1="0" y1="0" x2="1" y2="0">
        <stop offset="0" stop-color="#a8962e"/>
        <stop offset="0.5" stop-color="var(--gold-band)"/>
        <stop offset="1" stop-color="var(--yellow-band)"/>
      </linearGradient>
    </defs>

    <rect class="base" x="0" y="0" width="330" height="810" fill="var(--base-grey)"/>

    <rect class="lab-photo" x="0" y="0" width="330" height="340" fill="url(#labPhotoTone)"
          role="img" aria-label="Photo of a lab technician in a white coat and hair net looking through a microscope"/>

    <path class="brand-panel" d="M195,0 C228,30 232,80 252,100 C276,120 306,118 330,112 L330,0 Z"
          fill="var(--panel-grey)"/>
    <path class="brand-panel-edge" d="M252,100 C276,120 306,118 330,112"
          fill="none" stroke="var(--edge-teal)" stroke-width="2.5"/>
    <circle class="brand-mark" cx="287" cy="52" r="30" fill="#276e66"/>

    <path class="gold-wave" d="M100,377 C200,370 280,350 330,322 L330,356 C260,372 180,380 100,377 Z"
          fill="url(#goldWave)"/>

    <path class="teal-wave" d="M0,225 C70,255 140,290 220,292 C270,293 305,285 330,276 L330,330 C280,355 180,372 90,375 C50,377 20,377 0,376 Z"
          fill="url(#tealWave)"/>
    <path class="teal-wave-edge" d="M330,330 C280,355 180,372 90,375 C50,377 20,377 0,376"
          fill="none" stroke="var(--edge-teal)" stroke-width="2.5"/>

    <text class="headline">
      <tspan x="18" y="312">Custom Development of</tspan>
      <tspan x="18" y="333">Instruments and Software for:</tspan>
    </text>

    <g class="service-list">
      <g fill="var(--teal)">
        <circle cx="26" cy="410" r="4"/>
        <circle cx="26" cy="440" r="4"/>
        <circle cx="26" cy="470" r="4"/>
        <circle cx="26" cy="500" r="4"/>
        <circle cx="26" cy="530" r="4"/>
        <circle cx="26" cy="560" r="4"/>
        <circle cx="26" cy="590" r="4"/>
        <circle cx="26" cy="620" r="4"/>
      </g>
      <text x="40" y="416">Point-of-Care Readers</text>
      <text x="40" y="446">Lateral Flow Strips</text>
      <text x="40" y="476">Fluorescence</text>
      <text x="40" y="506">PCR</text>
      <text x="40" y="536">Thermal Activation</text>
      <text x="40" y="566">Fluidic Control</text>
      <text x="40" y="596">Electrochemistry</text>
      <text x="40" y="626">Immunoassays</text>
    </g>

    <path class="optics-photo" d="M0,665 C110,650 220,650 330,640 L330,750 L0,750 Z"
          fill="url(#opticsTone)"
          role="img" aria-label="Faint background photo of optical lenses and instrument software on a screen"/>

    <path class="footer-band" d="M0,810 L0,778 C8,755 28,742 60,742 L330,742 L330,810 Z"
          fill="var(--burgundy)"/>
    <text class="website" x="180" y="768" text-anchor="middle">www.qeltaoptic.example</text>
  </svg>
</div>
</body>
</html>
```